Sail Us to Harbourlight.co.nz .... Tourism business providing guided tours.

Design and build a website for our new company. The company is one where we take tourists to beautiful places for a fully guided tour for 2 weeks. Tours can follow our itinerary or be tailored to suit individual clients. .... Let us tell you a little of what we are about ....
Flying our clients to paradise for a ‘ Tailor Made ‘ tour or one where we organise everything and use our combined knowledge of more than 50 years experience in Indonesia where we travel to some of the places that are not well known on the tourist map, places that are often off the beaten track of tourists but that are spectacularly beautiful.
Our team .... Lucas Montrose (Ex Iron Fern), Gareth Thorne, Marisa Thorne & Sekar Purnama have reached a stage in life where making money is not essential but enjoying life is. We all have a passion to help others experience what we have when we travel to our paradise whether that is Indonesia, where we are starting our tours then we will be working on Thailand, Malaysia, Vietnam or New Zealand along with a number of other countries.
The experience of the ‘ Ladies ‘ in the team who are both native to the country along with my experience in the Film Production business where I have produced a number of documentaries on travelling through Indonesia and show casing the spectacular scenery there gives our clients access to what they will experience through my Vid Harbor channel. …. https://www.vidharbor.example/user/gthornefilm/videos
We claim to be the only tour company that produces documentaries on what our guests can expect to experience on their travels with us. All trips are personally guided with one of our team and we can also Taylor make trips where groups can be personally guided by the Ex Iron Fern in our team Lucas Montrose. Further to that we film and produce a Video of your trip as it happens ... that is something special that you get to keep and show friends & family.
To top that off we have Lucas Montrose on board who can call on his experience of travelling with the Iron Fern team but also his position as entertainment director for the IF’S on tour.
Lucas also has a vast experience as a host where he has hosted celebrities and entertained large companies which included Varnex the French aircraft maker and Heron Journal in Bali.
He has also been involved with organising events and hosting guests for the Prince and Princess of Monaco.
Sekar has a Batchelor degree in marketing and management and worked in the hotel industry and also runs Staynook villas where she is working on expanding that to the next level in Bali.
By chance we had been working on forming such a tour company individually and when we all realised this it was obvious we needed to form a company where we can call on our individual strengths.
The company will soon introduce other celebrity guides for our tours that will open opportunities for other ex players of International teams that are looking for opportunities when their playing careers finish.
What really stands out in Indonesia is the people - we consider they are the friendliest of all the countries we have travelled through. As a film maker I experience this throughout the country. When I intrude on peoples life and culture I am invariably met with a response that is so touching. The people of Indonesia are so proud of their way of life and equally as proud that I show such interest in their life. Our target market is clients that want to experience what we want to experience.
Bali is one part of our trip but the Island of Bali and the 17,200 other islands that make up the Indonesian Archipelago are what we have so much experience in travelling thru (some of - not all .... Yet?) and that is what makes our paradise the aim of the tours.
The company is currently being formed along with our Logo, brochures and a comprehensive website that will be online in a couple of weeks. Further to that and what in fact will be the main promotional tool for our company, we have a number of documentaries that will showcase ‘ Radiant Nusantara ‘ from the air and the ground that have been produced and are under production by our own in-house Film production company Quietcoastline pictures.
Links :https://www.vidharbor.example/watch?v=Qp7rTn2LmZk&feature=share&ref=Kd83JsPqWnRtYxLmZa92HvBcUeFgNiOpTsQwErTy&app=desktop
Our contact details :
‘ Sail Us to Harbourlight ‘ sailustoharbourlightnz@quillmail.example
Gareth & Marisa Thorne oakbarn_decor@kowhainet.example
Lucas Montrose: lmontrose17@quillmail.example

Target Market(s)

Older people with money to spend on holidays in Paradise .... We are adamant, at this stage that we are looking at the higher end of the market so that our tours are unique and not a crowded tour where all follow the leader. We want to retain the flexibility so that at the start of each day we can offer alternatives to what is on the itinerary. For example some of the group could go rafting and the ladies may prefer to go in another direction and to facilitate this we will have more than one vehicle on hand to do this.

Industry/Entity Type

Tourism

Coding

Coded - Design and coding required

Number of Pages Required

5+ page

Font styles to use
Serif

Colors
0792cd
85cae6
00a990

Requirements
Must have
• Buttons so prospective clients can book and pay for a trip
• Links to various Documentaries we have on out Vid Harbor Page .... Quietcoastline Pictures
• Contact details for each of the partners
Nice to have
• A similar site to https://www.tulipmarrtravel.example/premium-journeys/

```html
<!DOCTYPE html>
<html lang="en">
<head>
<meta charset="utf-8">
<title>Sail Us To Harbourlight – Guided Tours</title>
<link href="https://fonts.googleapis.com/css2?family=Exo+2:wght@400;500;600;700&family=Mulish:wght@400;600;700&display=swap" rel="stylesheet">
<style>
:root{
  --teal:#17a398;
  --teal-dark:#128b81;
  --navy:#0e2d6e;
  --navy-deep:#0a2460;
  --text:#555b66;
  --muted:#8a9099;
  --panel:#efefef;
  --line:#dcdcdc;
  --white:#ffffff;
  --footer:#1d2a2a;
}
*{box-sizing:border-box;margin:0;padding:0}
html,body{width:1200px;height:4489px;overflow:hidden}
body{position:relative;background:var(--white);font-family:"Mulish",Arial,sans-serif;color:var(--text)}
.abs{position:absolute}
h1,h2,h3,.heading{font-family:"Exo 2",Arial,sans-serif}

/* header */
.brand{left:75px;top:14px;display:flex;align-items:center;gap:10px}
.brand-dot{width:34px;height:34px;border-radius:50%;background:var(--navy)}
.brand-name{font-family:"Exo 2",sans-serif;font-weight:600;font-size:17px;color:var(--navy);line-height:1.05;width:170px}
.util{right:75px;top:30px;display:flex;align-items:center;gap:22px;font-size:14px;color:#444}
.lang{border:1px solid #ccc;padding:4px 8px;font-size:13px;display:flex;gap:10px;align-items:center}
.phone{display:flex;align-items:center;gap:8px;font-family:"Exo 2",sans-serif;font-size:30px;color:var(--teal)}
.nav{left:0;top:105px;width:1200px;height:60px;background:var(--teal)}
.nav ul{list-style:none;display:flex;position:absolute;left:78px;top:0;height:60px;align-items:center;gap:28px}
.nav li{color:var(--white);font-size:13.5px;font-weight:600;letter-spacing:.3px}
.enquire{left:909px;top:105px;width:159px;height:60px;background:var(--navy);color:var(--white);font-weight:700;font-size:15px;display:flex;align-items:center;justify-content:center}
.search{left:1068px;top:105px;width:57px;height:60px;display:flex;align-items:center;justify-content:center}

/* hero */
.hero{left:0;top:165px;width:1200px;height:515px;background:radial-gradient(ellipse at 55% 60%,#5fc3c0 0%,#2c8f99 35%,#1a5a63 65%,#0f3338 100%)}
.hero-box{left:270px;top:324px;width:666px;height:132px;background:rgba(40,55,60,.55);text-align:center;color:var(--white)}
.hero-box h1{font-weight:500;font-size:31px;margin-top:24px;letter-spacing:.5px}
.hero-box p{font-size:14px;margin-top:22px}
.play{left:555px;top:489px}

/* intro */
.welcome{left:78px;top:744px;font-size:17px;color:var(--teal);font-family:"Exo 2",sans-serif}
.intro-title{left:78px;top:770px;font-size:40px;font-weight:500;color:var(--navy)}
.intro-text{left:78px;top:834px;width:700px;font-size:13px;line-height:25px}
.exp-btn{height:54px;display:flex;align-items:center;justify-content:center;color:var(--white);font-size:14px;font-weight:600;background:var(--navy);width:240px}
.exp-btn.active{background:var(--teal)}
.included{left:825px;top:765px;width:300px;height:714px;background:var(--panel)}
.included h3{position:absolute;left:30px;top:36px;font-size:31px;font-weight:500;color:var(--teal)}
.included ul{position:absolute;left:30px;top:100px;width:255px;list-style:none}
.included li{position:relative;padding-left:26px;font-size:12px;line-height:17px;color:var(--text);margin-bottom:23px}
.included li svg{position:absolute;left:0;top:1px}
.share-label{left:855px;top:1352px;font-size:21px;font-weight:600;color:var(--navy);font-family:"Exo 2",sans-serif}
.socials{display:flex;gap:10px}
.soc{width:48px;height:48px;border-radius:50%}
.soc.a{background:#2b4a8a}.soc.b{background:#2aa0dc}.soc.c{background:#d9322a}.soc.d{background:#4d6e8e}

/* section titles */
.sec-title{left:0;width:1200px;text-align:center;font-size:46px;font-weight:600;color:var(--navy)}

/* tour cards */
.card{width:315px;height:540px;background:var(--white);border:1px solid var(--line)}
.card .photo{height:216px}
.card .country{position:absolute;left:18px;top:228px;font-size:17px;color:var(--teal);font-family:"Exo 2",sans-serif}
.card .rule{position:absolute;left:0;top:258px;width:100%;height:1px;background:var(--line)}
.card .days{position:absolute;left:22px;top:270px;color:var(--teal);font-family:"Exo 2",sans-serif;font-size:25px;line-height:24px}
.card .days small{display:block;font-size:13px}
.card .price{position:absolute;right:22px;top:270px;text-align:left;color:var(--teal);font-size:12px}
.card .price b{display:block;color:var(--navy);font-family:"Exo 2",sans-serif;font-size:25px;font-weight:600;margin-top:1px}
.card .body{position:absolute;left:0;top:330px;width:100%;height:209px;background:var(--panel)}
.card .body p{position:absolute;left:20px;top:24px;width:190px;font-size:12.5px;line-height:27px}
.card .btn{position:absolute;left:18px;top:147px;width:147px;height:45px;background:var(--navy);color:var(--white);font-weight:700;font-size:14px;display:flex;align-items:center;justify-content:center}

/* destinations */
.globe{left:393px;top:2880px;width:420px;height:420px;border-radius:50%;background:radial-gradient(circle at 40% 35%,#f4f4f4 0%,#d8d8d8 55%,#a9a9a9 100%)}
.dest{font-size:16px;color:#333;display:flex;align-items:center;gap:14px}
.dest i{width:12px;height:12px;border-radius:50%;background:var(--teal);display:block}

/* videos */
.vid-sub{left:0;top:3426px;width:1200px;text-align:center;font-size:13px;color:var(--muted)}
.band-teal{left:0;top:3690px;width:1200px;height:465px;background:var(--teal)}
.side-photo-l{left:0;top:3534px;width:315px;height:315px;background:linear-gradient(180deg,#a9cde0 0%,#d8e4e2 35%,#3c7b62 50%,#d9cdb0 70%,#c8b896 100%)}
.side-photo-r{left:888px;top:3534px;width:312px;height:315px;background:linear-gradient(180deg,#9cbed0 0%,#6f9a93 35%,#2f6a6c 60%,#4f8f8a 100%)}
.vid-frame{left:315px;top:3495px;width:573px;height:396px;background:var(--navy-deep)}
.vid-thumb{left:366px;top:3555px;width:474px;height:279px;background:linear-gradient(180deg,#8fc1e4 0%,#b8d8ee 45%,#d8cfc0 75%,#b9a88e 100%)}
.vid-play{left:570px;top:3668px}

/* newsletter */
.news-title{left:0;top:3942px;width:1200px;text-align:center;font-size:38px;font-weight:500;color:var(--white);letter-spacing:.5px}
.news-sub{left:0;top:3993px;width:1200px;text-align:center;font-size:13px;color:var(--white)}
.news-input{left:249px;top:4035px;width:561px;height:54px;background:var(--white);font-size:12px;color:#999;padding:19px 22px}
.news-btn{left:810px;top:4035px;width:156px;height:54px;background:var(--navy);color:var(--white);font-weight:700;font-size:15px;display:flex;align-items:center;justify-content:center}

/* footer */
.footer{left:0;top:4155px;width:1200px;height:334px;background:linear-gradient(180deg,#243634 0%,#1a2726 50%,#142020 100%)}
.f-col{list-style:none;font-size:12.5px;color:#cfd6d6;line-height:30px}
.brochure{width:84px;height:111px}
.req-btn{left:765px;top:4329px;width:282px;height:51px;background:var(--navy);color:var(--white);font-weight:700;font-size:14px;display:flex;align-items:center;justify-content:center}
.f-rule{left:78px;top:4425px;width:1047px;height:1px;background:rgba(255,255,255,.2)}
.copy{left:78px;top:4455px;font-size:12px;color:#cfd6d6}
.f-soc{width:36px;height:36px}
</style>
</head>
<body>

<!-- header -->
<div class="abs brand"><span class="brand-dot"></span><span class="brand-name">SAIL US TO HARBOURLIGHT</span></div>
<div class="abs util">
  <span>Brochures</span><span>Contact Us</span>
  <span class="lang">NZ <svg width="9" height="6" viewBox="0 0 9 6"><path d="M0 0h9L4.5 6z" fill="#444"/></svg></span>
  <span class="phone"><svg width="26" height="26" viewBox="0 0 24 24"><circle cx="12" cy="12" r="11" fill="none" stroke="#17a398" stroke-width="2"/><path d="M8 6.5l2 .3.8 2.6-1.3 1.1a7 7 0 0 0 4 4l1.1-1.3 2.6.8.3 2a1.5 1.5 0 0 1-1.6 1.4A10 10 0 0 1 6.6 8.1 1.5 1.5 0 0 1 8 6.5z" fill="#17a398"/></svg>123 456 7890</span>
</div>
<nav class="abs nav">
  <ul><li>DESTINATIONS</li><li>TOURS</li><li>TAILOR-MADE</li><li>SPECIAL OFFERS</li><li>ABOUT US</li><li>BEFORE YOU GO</li><li>REVIEWS</li></ul>
</nav>
<div class="abs enquire">ENQUIRE NOW</div>
<div class="abs search"><svg width="20" height="20" viewBox="0 0 20 20"><circle cx="8" cy="8" r="6" fill="none" stroke="#fff" stroke-width="2.6"/><path d="M12.5 12.5L18 18" stroke="#fff" stroke-width="2.8" stroke-linecap="round"/></svg></div>

<!-- hero -->
<div class="abs hero" role="img" aria-label="Aerial photo of turquoise lagoons and forested tropical islands"></div>
<div class="abs hero-box"><h1>50 YEARS EXPERIENCE IN INDONESIA</h1><p>Lorem Ipsum is simply dummy text of the printing and typesetting industry.</p></div>
<svg class="abs play" width="90" height="90" viewBox="0 0 90 90"><circle cx="45" cy="45" r="42" fill="none" stroke="#fff" stroke-width="4"/><path d="M36 28l26 17-26 17z" fill="#fff"/></svg>

<!-- intro -->
<div class="abs welcome">Welcome To</div>
<h2 class="abs intro-title">Sail Us To Harbourlight</h2>
<p class="abs intro-text">Lorem Ipsum is simply dummy text of the printing and typesetting industry. Lorem Ipsum has been the industry's standard dummy text ever since the 1500s, when an unknown printer took a galley of type and scrambled it to make a type specimen book. It has survived not only five centuries, but also the leap into electronic typesetting, remaining essentially unchanged.Lorem Ipsum is simply dummy text of the printing and typesetting industry. Lorem Ipsum has been the industry's standard dummy text ever since the 1500s, when an unknown printer took a galley of type and scrambled it to make a type specimen book.</p>
<div class="abs exp-btn active" style="left:78px;top:1050px">INDONESIA EXPERIENCE</div>
<div class="abs exp-btn" style="left:333px;top:1050px">THAILAND EXPERIENCE</div>
<div class="abs exp-btn" style="left:78px;top:1113px">MALAYSIA EXPERIENCE</div>
<div class="abs exp-btn" style="left:333px;top:1113px">VIETNAM EXPERIENCE</div>
<div class="abs exp-btn" style="left:78px;top:1176px">ZEALAND EXPERIENCE</div>

<aside class="abs included">
  <h3>Whats Include</h3>
  <ul>
    <li><svg width="15" height="15" viewBox="0 0 15 15"><circle cx="7.5" cy="7.5" r="6.5" fill="none" stroke="#17a398" stroke-width="1.5"/><path d="M4.5 7.7l2 2 4-4" fill="none" stroke="#17a398" stroke-width="1.5"/></svg>Return international economy flights, taxes and current fuel surcharges (subject to change)</li>
    <li><svg width="15" height="15" viewBox="0 0 15 15"><circle cx="7.5" cy="7.5" r="6.5" fill="none" stroke="#17a398" stroke-width="1.5"/><path d="M4.5 7.7l2 2 4-4" fill="none" stroke="#17a398" stroke-width="1.5"/></svg>Deluxe accommodation</li>
    <li><svg width="15" height="15" viewBox="0 0 15 15"><circle cx="7.5" cy="7.5" r="6.5" fill="none" stroke="#17a398" stroke-width="1.5"/><path d="M4.5 7.7l2 2 4-4" fill="none" stroke="#17a398" stroke-width="1.5"/></svg>Exclusive touring and dining experiences</li>
    <li><svg width="15" height="15" viewBox="0 0 15 15"><circle cx="7.5" cy="7.5" r="6.5" fill="none" stroke="#17a398" stroke-width="1.5"/><path d="M4.5 7.7l2 2 4-4" fill="none" stroke="#17a398" stroke-width="1.5"/></svg>All transportation</li>
    <li><svg width="15" height="15" viewBox="0 0 15 15"><circle cx="7.5" cy="7.5" r="6.5" fill="none" stroke="#17a398" stroke-width="1.5"/><path d="M4.5 7.7l2 2 4-4" fill="none" stroke="#17a398" stroke-width="1.5"/></svg>Sightseeing with the experts</li>
    <li><svg width="15" height="15" viewBox="0 0 15 15"><circle cx="7.5" cy="7.5" r="6.5" fill="none" stroke="#17a398" stroke-width="1.5"/><path d="M4.5 7.7l2 2 4-4" fill="none" stroke="#17a398" stroke-width="1.5"/></svg>Expert National Experts and knowledgeable local guides</li>
    <li><svg width="15" height="15" viewBox="0 0 15 15"><circle cx="7.5" cy="7.5" r="6.5" fill="none" stroke="#17a398" stroke-width="1.5"/><path d="M4.5 7.7l2 2 4-4" fill="none" stroke="#17a398" stroke-width="1.5"/></svg>Visa fees for New Zealand passport holders</li>
    <li><svg width="15" height="15" viewBox="0 0 15 15"><circle cx="7.5" cy="7.5" r="6.5" fill="none" stroke="#17a398" stroke-width="1.5"/><path d="M4.5 7.7l2 2 4-4" fill="none" stroke="#17a398" stroke-width="1.5"/></svg>Specialist advice from our experienced travel consultants</li>
    <li><svg width="15" height="15" viewBox="0 0 15 15"><circle cx="7.5" cy="7.5" r="6.5" fill="none" stroke="#17a398" stroke-width="1.5"/><path d="M4.5 7.7l2 2 4-4" fill="none" stroke="#17a398" stroke-width="1.5"/></svg>Champagne moments and small group sizes of 18 or less</li>
  </ul>
</aside>
<div class="abs share-label">Share</div>
<div class="abs socials" style="left:855px;top:1395px" aria-label="Share links">
  <span class="soc a"></span><span class="soc b"></span><span class="soc c"></span><span class="soc d"></span>
</div>

<!-- deluxe tours -->
<h2 class="abs sec-title" style="top:1524px">Our Deluxe Tours Are</h2>

<article class="abs card" style="left:99px;top:1620px"><div class="photo" role="img" aria-label="Aerial photo of a jungle island and blue sea" style="background:linear-gradient(160deg,#3f9fd0,#2f8a6a 45%,#6ec6d0 75%,#1e6fa8)"></div><span class="country">Indonesia</span><span class="rule"></span><div class="days">16<small>Days</small></div><div class="price">From<b>$9,582pp</b></div><div class="body"><p>Lorem Ipsum is simply text of the printing and type setting industry.</p><span class="btn">VIEW TOUR</span></div></article>
<article class="abs card" style="left:444px;top:1620px"><div class="photo" role="img" aria-label="Aerial photo of a lagoon and reef" style="background:linear-gradient(170deg,#1d4f7a,#4fa7a4 50%,#2b6a8c)"></div><span class="country">Vietnam</span><span class="rule"></span><div class="days">16<small>Days</small></div><div class="price">From<b>$9,582pp</b></div><div class="body"><p>Lorem Ipsum is simply text of the printing and type setting industry.</p><span class="btn">VIEW TOUR</span></div></article>
<article class="abs card" style="left:789px;top:1620px"><div class="photo" role="img" aria-label="Aerial photo of green islets in shallow water" style="background:linear-gradient(165deg,#5aa36b,#3e9aa0 45%,#2d7aa0)"></div><span class="country">Malaysia</span><span class="rule"></span><div class="days">16<small>Days</small></div><div class="price">From<b>$9,582pp</b></div><div class="body"><p>Lorem Ipsum is simply text of the printing and type setting industry.</p><span class="btn">VIEW TOUR</span></div></article>

<article class="abs card" style="left:99px;top:2199px"><div class="photo" role="img" aria-label="Aerial photo of a coastal village and sea" style="background:linear-gradient(170deg,#9cb6c8,#4d7a55 40%,#2f6f86)"></div><span class="country">Indonesia</span><span class="rule"></span><div class="days">16<small>Days</small></div><div class="price">From<b>$9,582pp</b></div><div class="body"><p>Lorem Ipsum is simply text of the printing and type setting industry.</p><span class="btn">VIEW TOUR</span></div></article>
<article class="abs card" style="left:444px;top:2199px"><div class="photo" role="img" aria-label="Aerial photo of a small island ringed with sand" style="background:radial-gradient(ellipse at 50% 55%,#4f8a4c 0%,#d9d3b8 22%,#3fb0b0 40%,#1b5f7a 100%)"></div><span class="country">Vietnam</span><span class="rule"></span><div class="days">16<small>Days</small></div><div class="price">From<b>$9,582pp</b></div><div class="body"><p>Lorem Ipsum is simply text of the printing and type setting industry.</p><span class="btn">VIEW TOUR</span></div></article>
<article class="abs card" style="left:789px;top:2199px"><div class="photo" role="img" aria-label="Photo of karst islands and palm trees under blue sky" style="background:linear-gradient(180deg,#3f7fc8,#8fb8e0 40%,#2f5f3e 60%,#1e4d5a)"></div><span class="country">Malaysia</span><span class="rule"></span><div class="days">16<small>Days</small></div><div class="price">From<b>$9,582pp</b></div><div class="body"><p>Lorem Ipsum is simply text of the printing and type setting industry.</p><span class="btn">VIEW TOUR</span></div></article>

<!-- destinations -->
<h2 class="abs sec-title" style="top:2795px">Our Destination</h2>
<div class="abs globe" role="img" aria-label="Grey globe map with a highlighted destination"></div>
<div class="abs dest" style="left:276px;top:2960px">Indonesia <i></i></div>
<div class="abs dest" style="left:240px;top:3080px">Malaysia <i></i></div>
<div class="abs dest" style="left:291px;top:3206px">Thailand <i></i></div>
<div class="abs dest" style="left:813px;top:2960px"><i></i> Vietnam</div>
<div class="abs dest" style="left:879px;top:3080px"><i></i> New Zealand</div>

<!-- videos -->
<h2 class="abs sec-title" style="top:3365px">Watch Videos</h2>
<p class="abs vid-sub">Lorem Ipsum simple text of print and type industry !</p>
<div class="abs band-teal"></div>
<div class="abs side-photo-l" role="img" aria-label="Photo of a beach with people walking by the shore"></div>
<div class="abs side-photo-r" role="img" aria-label="Photo of karst islands in a turquoise bay"></div>
<div class="abs vid-frame"></div>
<div class="abs vid-thumb" role="img" aria-label="Video still of two travellers on a tropical beach"></div>
<svg class="abs vid-play" width="66" height="66" viewBox="0 0 66 66"><circle cx="33" cy="33" r="32" fill="rgba(14,45,110,.85)"/><path d="M26 20l22 13-22 13z" fill="#fff"/></svg>

<!-- newsletter -->
<h2 class="abs news-title">SIGN UP OUR NEWSLETTER</h2>
<p class="abs news-sub">Would you like to receive our exclusive news and update for sign up our newsletter!</p>
<div class="abs news-input">Enter Email *</div>
<div class="abs news-btn">SUBSCRIBE</div>

<!-- footer -->
<footer class="abs footer" role="img" aria-label="Dark photo of tropical foliage behind the footer"></footer>
<ul class="abs f-col" style="left:78px;top:4188px"><li>Our Philosophy</li><li>Why Book with Us?</li><li>Price Promise</li><li>Contact Us</li><li>Blog</li></ul>
<ul class="abs f-col" style="left:288px;top:4188px"><li>Booking Conditions</li><li>Privacy Policy</li><li>Customer Reviews</li><li>FAQ's</li><li>Customer Service</li></ul>
<ul class="abs f-col" style="left:498px;top:4188px"><li>Indonesian Tour</li><li>Vietnam Tours</li><li>Malaysia Tours</li><li>Thailand Tours</li><li>New Zealand</li></ul>
<div class="abs brochure" style="left:711px;top:4191px;background:linear-gradient(180deg,#e8e2d6,#8a9a8a)" role="img" aria-label="Brochure cover"></div>
<div class="abs brochure" style="left:816px;top:4191px;background:linear-gradient(180deg,#c9553a,#6b3a2e)" role="img" aria-label="Brochure cover"></div>
<div class="abs brochure" style="left:921px;top:4191px;background:linear-gradient(180deg,#f2efe8,#8fb0c4)" role="img" aria-label="Brochure cover"></div>
<div class="abs brochure" style="left:1026px;top:4191px;background:linear-gradient(180deg,#e4e8ee,#3e7aa8)" role="img" aria-label="Brochure cover"></div>
<div class="abs req-btn">REQUEST A BROCHURE NOW</div>
<div class="abs f-rule"></div>
<div class="abs copy">©Sail Us To Harbourlight – 2019 All Rights reserved</div>
<div class="abs socials" style="left:945px;top:4446px;gap:9px">
  <span class="soc a f-soc"></span><span class="soc b f-soc"></span><span class="soc c f-soc"></span><span class="soc d f-soc"></span>
</div>

</body>
</html>
```